BHAG Poster

We like creativity and visual boxes and shapes not just bullet points. We think we want it to be landscape view. Here are some of the parameters:

BHAG:
Become one of the most admired construction companies in the markets we serve within the next 10 years

3 – 5 year goals:
1. Generate 35m in revenue by 2020
2. Have a 50/50 mix of Public-Private job mix
3. Maintain 15% annual growth

1 year goals:
1. $24M in revenue with better margins
2. 14% gross margin on year
3. Business development begins to pay off
4. Continue recruiting great & talented people

Dynamic Quarter Goal:
(Leave this area blank so we can fill it in each quarter please)

Industry/Entity Type

Landscape

Colors
0355a3

Requirements
Must have
• SHAPES OR BOXES FOR VISUAL EFFECT. We don't want it to just be words on a page. Must be creative. Must have our logo somewhere on the poster. Our cmyk blue color is 100-80-0-22. Poster can have different colors, but it just needs to have some of our blue in it.
Should not have
• no bullet points

```html
<!DOCTYPE html>
<html lang="en">
<head>
<meta charset="utf-8">
<title>BHAG Poster – Halvorsen Construction</title>
<link rel="stylesheet" href="https://fonts.googleapis.com/css2?family=Montserrat:wght@700;800&family=Oswald:wght@300;400&family=Roboto:wght@700&display=swap">
<style>
  :root {
    --bg-dark: #2a2a2a;
    --bg-dark-2: #333333;
    --panel: #a9a9a9;
    --panel-2: #b8b8b8;
    --panel-line: #c9c9c9;
    --quarter-text: #e0e0e0;
    --white: #ffffff;
    --text-light: #e9e9e9;
    --logo-grey: #bdbdbd;
    --green: #45b649;
    --green-bright: #22c55e;
    --sky: #00aeef;
    --sky-text: #2a9df4;
    --brand-blue: #2457a6;
    --mix-blue: #2d8ef0;
  }
  * { box-sizing: border-box; margin: 0; padding: 0; }
  html, body { width: 1200px; height: 798px; overflow: hidden; background: var(--bg-dark); }
  .poster {
    position: relative;
    width: 1200px; height: 798px;
    background: radial-gradient(ellipse at 50% 35%, var(--bg-dark-2), var(--bg-dark) 75%);
    font-family: "Oswald", sans-serif;
    color: var(--text-light);
  }
  .centered { position: absolute; transform: translateX(-50%); text-align: center; white-space: nowrap; }

  .brand {
    top: 50px; left: 598px;
    display: flex; align-items: center; gap: 8px;
    font-family: "Oswald", sans-serif; font-weight: 400;
    font-size: 27px; letter-spacing: 0.5px; color: var(--logo-grey);
  }
  .brand-square { width: 30px; height: 30px; background: var(--logo-grey); }

  .goal-figure {
    font-family: "Montserrat", sans-serif; font-weight: 800;
    font-size: 36px; line-height: 1; letter-spacing: 0.5px;
  }
  .goal-top .goal-figure { top: 142px; }
  .goal-caption {
    font-weight: 300; font-size: 22px; line-height: 36px;
    text-transform: uppercase; letter-spacing: -0.3px;
  }
  .goal-top .goal-caption { top: 186px; }
  .goal-bottom .goal-figure { top: 442px; }
  .goal-bottom .goal-caption { top: 488px; line-height: 27px; }

  .fig-green { color: var(--green-bright); }
  .fig-sky { color: var(--sky-text); }
  .fig-white { color: var(--white); }
  .fig-mix { color: var(--mix-blue); }

  .timeline { position: absolute; left: 0; top: 0; }
  .stage-label {
    font-family: "Montserrat", sans-serif; font-weight: 700;
    font-size: 22px; fill: var(--white);
  }

  .goal-icon { position: absolute; transform: translateX(-50%); top: 436px; }

  .quarters {
    position: absolute; left: 0; top: 594px; width: 1200px; height: 204px;
    display: grid; grid-template-columns: 318px 294px 294px 294px;
    background: linear-gradient(180deg, var(--panel-2), var(--panel));
  }
  .quarter {
    display: flex; align-items: center; justify-content: center;
    border-left: 1px solid var(--panel-line);
    font-family: "Roboto", sans-serif; font-weight: 700;
    font-size: 50px; color: var(--quarter-text);
    padding-bottom: 20px;
  }
  .quarter:first-child { border-left: none; }
</style>
</head>
<body>
<main class="poster">

  <div class="brand centered"><span class="brand-square"></span><span>HALVORSEN CONSTRUCTION</span></div>

  <section class="goal-top">
    <div class="goal-figure fig-green centered" style="left:286px">$24M</div>
    <div class="goal-caption centered" style="left:287px">In revenue with<br>better margins</div>

    <div class="goal-figure fig-green centered" style="left:470px">14%</div>
    <div class="goal-caption centered" style="left:469px">Gross margin<br>on year</div>

    <div class="goal-figure fig-sky centered" style="left:660px">$35M</div>
    <div class="goal-caption centered" style="left:660px">Revenue by 2020</div>

    <div class="goal-figure fig-white centered" style="left:914px">BAGH</div>
    <div class="goal-caption centered" style="left:917px">Become one of the most admired<br>companies in the markets we serve</div>
  </section>

  <svg class="timeline" width="1200" height="440" viewBox="0 0 1200 440" aria-hidden="true">
    <g fill="var(--white)" stroke="var(--white)" stroke-width="3">
      <line x1="287" y1="272" x2="287" y2="306"/>
      <line x1="471" y1="272" x2="471" y2="306"/>
      <line x1="660" y1="272" x2="660" y2="306"/>
      <line x1="916" y1="272" x2="916" y2="306"/>
      <line x1="212" y1="384" x2="212" y2="416"/>
      <line x1="398" y1="384" x2="398" y2="416"/>
      <line x1="596" y1="384" x2="596" y2="416"/>
      <line x1="796" y1="384" x2="796" y2="416"/>
    </g>
    <g fill="var(--white)">
      <circle cx="287" cy="271" r="7"/>
      <circle cx="471" cy="271" r="7"/>
      <circle cx="660" cy="271" r="7"/>
      <circle cx="916" cy="271" r="7"/>
      <circle cx="212" cy="418" r="7"/>
      <circle cx="398" cy="418" r="7"/>
      <circle cx="596" cy="418" r="7"/>
      <circle cx="796" cy="418" r="7"/>
    </g>

    <polygon points="992,321 1066,321 1094,348 1066,374 992,374 1020,348" fill="var(--white)"/>
    <polygon points="816,321 998,321 1026,348 998,374 816,374 842,348" fill="var(--brand-blue)"/>
    <polygon points="524,321 816,321 844,348 816,374 524,374 550,348" fill="var(--sky)"/>
    <polygon points="164,321 520,321 546,348 520,374 164,374 192,348" fill="var(--green)"/>
    <polygon points="92,321 164,321 194,348 164,374 92,374 120,348" fill="var(--white)"/>

    <text class="stage-label" x="356" y="356" text-anchor="middle">1 YEAR</text>
    <text class="stage-label" x="679" y="356" text-anchor="middle">3–5 YEARS</text>
    <text class="stage-label" x="925" y="356" text-anchor="middle">10 YEARS</text>
  </svg>

  <section class="goal-bottom">
    <svg class="goal-icon" style="left:212px" width="56" height="38" viewBox="0 0 56 38" aria-hidden="true">
      <g fill="var(--green-bright)">
        <polygon points="0,6 10,2 18,22 8,26"/>
        <polygon points="56,6 46,2 38,22 48,26"/>
        <path d="M14,8 L26,6 L34,10 L44,8 L42,22 L30,34 Q26,36 22,32 L16,24 Z"/>
      </g>
    </svg>
    <div class="goal-caption centered" style="left:212px">Business development<br>begins to pay off</div>

    <svg class="goal-icon" style="left:400px" width="58" height="40" viewBox="0 0 58 40" aria-hidden="true">
      <g fill="var(--green-bright)">
        <circle cx="14" cy="9" r="6"/>
        <circle cx="44" cy="9" r="6"/>
        <path d="M2,36 Q2,18 14,18 Q26,18 26,36 Z"/>
        <path d="M32,36 Q32,18 44,18 Q56,18 56,36 Z"/>
        <circle cx="29" cy="8" r="7"/>
        <path d="M15,40 Q15,18 29,18 Q43,18 43,40 Z"/>
      </g>
    </svg>
    <div class="goal-caption centered" style="left:399px">Recruit great<br>and talent</div>

    <div class="goal-figure fig-sky centered" style="left:594px">15%</div>
    <div class="goal-caption centered" style="left:594px">Annual growth<br>rate</div>

    <div class="goal-figure fig-mix centered" style="left:799px">50/50</div>
    <div class="goal-caption centered" style="left:797px">Public / private<br>job mix</div>
  </section>

  <section class="quarters">
    <div class="quarter">Q1</div>
    <div class="quarter">Q2</div>
    <div class="quarter">Q3</div>
    <div class="quarter">Q4</div>
  </section>

</main>
</body>
</html>
```